Provide bookkeeping and accounting services to small and growing businesses

We need website and logo design using the name Daltonby as the logo.
The target audience are small companies and startups who need:
1) Simple bookkeeping services
2) Accounting advice that only someone with many years of senior financial experience as a CPA can provide.

The services are provided by two individuals. each of whom specialize in one of the areas.

We want the website to be clean without a lot of visual distraction but don't know how to make a boring subject interesting. We believe our potential clients, small business owners, need to find what they want quickly and easily without a lot of verbiage or distractions.

We've attached a draft of the homepage and have completed the text on most of the other pages.

Target Market(s)

small and early stage growth companies in San Diego North County

Industry/Entity Type

Accounting

Number of Pages Required

1 page

Font styles to use
Sans Serif

Colors
86cfc6
33b8a4
85cae6

Requirements
Must have
• We need a design for the website homepage that includes the name Daltonby as the logo. Must include a design for the name.
• Must have color in teal or greenish blue.
Nice to have
• White background, clean, clear, uncluttered.
• We would like to use the design in a Theme on a WordPress website. Themes Maple Harbor and Copper Lantern are appealing to us.
Should not have
• Moving pictures

```html
<!DOCTYPE html>
<html lang="en">
<head>
<meta charset="utf-8">
<title>Daltonby Bookkeeping</title>
<link href="https://fonts.googleapis.com/css2?family=Signika:wght@300;400&family=Raleway:wght@400;500;600;700&family=Lato:ital,wght@0,400;0,700;1,400&display=swap" rel="stylesheet">
<style>
:root{
  --teal:#33b8a4;
  --teal-soft:#86cfc6;
  --sky:#85cae6;
  --topbar:#0f3a4e;
  --ink:#2b2b2b;
  --text:#444;
  --muted:#777;
  --band:#f4f4f4;
  --partner-band:#eef9fb;
  --footer:#2e2e2e;
  --footer-base:#262626;
  --line:#cfcfcf;
}
*{box-sizing:border-box;margin:0;padding:0}
html,body{width:1200px;height:2439px;overflow:hidden;background:#fff}
body{position:relative;font-family:"Lato",sans-serif;color:var(--text)}
.abs{position:absolute}
h2,h3{font-weight:400}

/* top bar */
.topbar{left:0;top:0;width:1200px;height:34px;background:var(--topbar);color:#fff;font-size:13px;font-weight:700}
.topbar .item{position:absolute;top:0;height:34px;display:flex;align-items:center;gap:9px}
.topbar svg{width:19px;height:19px}

/* header */
.header{left:0;top:34px;width:1200px;height:85px;background:#fff}
.logo{position:absolute;left:101px;top:14px;font-family:"Raleway",sans-serif}
.logo .name{font-size:37px;font-weight:700;color:var(--teal);line-height:1;letter-spacing:.5px}
.logo .tag{font-size:14px;font-weight:600;color:var(--ink);letter-spacing:5.2px;margin-top:4px}
.nav a{position:absolute;top:28px;height:30px;line-height:30px;font-family:"Raleway",sans-serif;font-size:14px;color:#333;text-decoration:none}
.nav a.active{background:var(--teal);color:#fff;padding:0 14px;font-weight:600}

/* hero */
.hero{left:0;top:119px;width:1200px;height:515px;background:linear-gradient(120deg,#1b2a33 0%,#3f5866 35%,#8aa2ad 55%,#4b6370 75%,#1d2b33 100%)}
.hero-title{left:0;top:352px;width:1200px;text-align:center;font-family:"Raleway",sans-serif;font-size:33px;font-weight:600;color:var(--teal-soft)}
.hero-sub{left:0;top:406px;width:1200px;text-align:center;font-family:"Raleway",sans-serif;font-size:17px;font-weight:700;color:#fff}
.hero-arrow{width:34px;height:34px;top:360px}

/* section headings */
.sec-title{width:1200px;left:0;text-align:center;font-family:"Signika",sans-serif;font-weight:300;font-size:32px;color:var(--ink)}
.sec-title span,.col-title span{color:var(--teal)}
.divider{height:12px}
.divider .rule{position:absolute;top:5px;height:1px;background:var(--line)}
.divider .dot{position:absolute;top:2px;width:8px;height:8px;border-radius:50%;border:1px solid #999;background:#fff}
.divider .dot.mid{background:#999}

/* about */
.about-text{left:114px;top:752px;width:972px;text-align:center;font-size:13.4px;line-height:24.5px;color:#222}
.btn{background:var(--teal-soft);color:#fff;font-family:"Raleway",sans-serif;font-weight:700;font-size:15px;text-align:center;border-radius:2px}

/* services */
.services{left:0;top:925px;width:1200px;height:454px;background:var(--band)}
.service{position:absolute;top:1064px;width:260px;text-align:center}
.service .ring{margin:0 auto;width:116px;height:116px;border-radius:50%;background:#fff;box-shadow:0 3px 8px rgba(0,0,0,.12),inset 0 0 0 10px #f1f1f1;display:flex;align-items:center;justify-content:center}
.service h3{margin-top:33px;font-family:"Raleway",sans-serif;font-size:16.5px;font-weight:700;color:#222}
.service p{margin-top:9px;font-size:13px;line-height:21px;color:#555}
.service .btn{display:inline-block;margin-top:10px;width:112px;height:33px;line-height:33px}
.svc-sep{top:1080px;width:1px;height:240px;background:#e2e2e2}

/* testimonials & contact */
.col-title{font-family:"Signika",sans-serif;font-weight:300;font-size:32px;color:var(--ink)}
.quote-box{left:101px;top:1520px;width:512px;height:239px;background:#fafafa;border:1px solid #e3e3e3;border-radius:6px;box-shadow:0 2px 5px rgba(0,0,0,.08)}
.quote-text{left:122px;top:1546px;width:462px;font-size:13.3px;line-height:24.6px;font-style:italic;color:#333}
.quote-mark{font-family:"Signika",sans-serif;font-style:normal;font-size:44px;color:#d2d2d2;line-height:0;vertical-align:-14px}
.avatar{left:125px;top:1709px;width:112px;height:112px;border-radius:50%;background:linear-gradient(160deg,#a9b9c7,#5d7a96);border:6px solid #fff;box-shadow:0 0 0 1px #ddd}
.client-name{left:260px;top:1774px;font-family:"Raleway",sans-serif;font-weight:700;font-size:15px;color:var(--teal)}
.field{left:758px;width:343px;height:33px;border:1px solid #cfcfcf;background:#fff;font-size:13px;color:#333;padding:8px 10px}
.submit{left:758px;top:1785px;width:112px;height:36px;line-height:36px}

/* partners */
.partners{left:0;top:1862px;width:1200px;height:296px;background:var(--partner-band)}
.badge{top:2002px;height:100px;background:#fff;border:1px solid #e4e4e4;display:flex;align-items:center;justify-content:center}
.badge i{display:block;width:110px;height:34px;border-radius:4px;background:#d9d9d9}

/* footer */
.footer{left:0;top:2158px;width:1200px;height:234px;background:var(--footer)}
.footer-base{left:0;top:2392px;width:1200px;height:47px;background:var(--footer-base);border-top:1px solid #3d3d3d;color:#bbb;font-size:13px}
.f-title{font-family:"Raleway",sans-serif;font-size:17px;color:#fff;padding-bottom:8px;border-bottom:1px solid #555}
.f-list{list-style:none;color:#fff;font-size:13px;line-height:24.5px;margin-top:8px}
.f-list li::before{content:"›";margin-right:7px}
.f-text{color:#eee;font-size:13px;line-height:21px}
.f-vsep{top:2197px;width:1px;height:170px;background:#444}
.social{display:flex;align-items:center;gap:10px;color:#fff;font-size:10px;letter-spacing:.8px;height:36px}
.social i{width:14px;height:14px;border-radius:50%;background:#fff;display:block}
.news-art{left:760px;top:2226px;width:70px;height:62px;background:linear-gradient(135deg,#e6e6e6,#9a9a9a);border-radius:3px}
.news-input{left:611px;top:2307px;width:155px;height:33px;background:#fff;font-size:13px;color:#333;padding:8px 10px 0 30px}
.news-btn{left:766px;top:2307px;width:100px;height:33px;line-height:33px;background:var(--teal);color:#fff;font-family:"Raleway",sans-serif;font-size:13px;font-weight:700;text-align:center}
</style>
</head>
<body>

<!-- top bar -->
<div class="abs topbar">
  <div class="item" style="left:716px">
    <svg viewBox="0 0 20 20"><circle cx="10" cy="10" r="9" fill="#fff"/><rect x="5" y="6.5" width="10" height="7" fill="var(--topbar)"/><path d="M5 6.5l5 4 5-4" stroke="#fff" stroke-width="1" fill="none"/></svg>
    info@daltonbybookkeeping.com
  </div>
  <div class="item" style="left:975px">
    <svg viewBox="0 0 20 20"><circle cx="10" cy="10" r="8.5" fill="none" stroke="#fff" stroke-width="1.5"/><path d="M7 5.5l2 2-1 1.3c.6 1.4 1.6 2.5 3 3.1l1.3-1 2 2-1.2 1.4c-3.3-.3-6.2-3.2-6.6-6.6z" fill="#fff"/></svg>
    555-014-2290
  </div>
</div>

<!-- header -->
<header class="abs header">
  <div class="logo">
    <div class="name">Daltonby</div>
    <div class="tag">BOOKKEEPING</div>
  </div>
  <nav class="nav">
    <a class="active" style="left:474px">Home</a>
    <a style="left:576px">About Us</a>
    <a style="left:682px">Services</a>
    <a style="left:785px">Experience</a>
    <a style="left:906px">Resources</a>
    <a style="left:1024px">Contact Us</a>
  </nav>
</header>

<!-- hero -->
<div class="abs hero" role="img" aria-label="Blurred office photo: laptop and financial charts on a desk with business people talking by a window"></div>
<div class="abs hero-title">Accounting And Bookkeeping Services And Support</div>
<div class="abs hero-sub">For Small And Growing Organizations In San Diego North County</div>
<svg class="abs hero-arrow" style="left:39px" viewBox="0 0 34 34"><circle cx="17" cy="17" r="15.5" fill="none" stroke="#fff" stroke-width="1.5"/><path d="M19.5 11l-6 6 6 6" stroke="#fff" stroke-width="1.8" fill="none"/></svg>
<svg class="abs hero-arrow" style="left:1127px" viewBox="0 0 34 34"><circle cx="17" cy="17" r="15.5" fill="none" stroke="#fff" stroke-width="1.5"/><path d="M14.5 11l6 6-6 6" stroke="#fff" stroke-width="1.8" fill="none"/></svg>

<!-- about -->
<h2 class="abs sec-title" style="top:672px">About <span>Daltonby Bookkeeping</span></h2>
<div class="abs divider" style="left:0;top:721px;width:1200px">
  <div class="rule" style="left:397px;width:406px"></div>
  <div class="dot" style="left:578px"></div><div class="dot mid" style="left:596px"></div><div class="dot" style="left:614px"></div>
</div>
<p class="abs about-text">Lorem ipsum dolor sit amet, consectetur adipiscing elit, sed do eiusmod tempor incididunt ut labore et dolore magna aliqua. Ut enim ad minim veniam, quis nostrud exercitation ullamco laboris nisi ut aliquip ex ea commodo consequat. Duis aute irure dolor in reprehenderit in voluptate velit esse cillum dolore eu fugiat nulla pariatur. Excepteur sint occaecat cupidatat non proident, sunt in culpa qui officia deserunt mollit anim id est laborum.</p>
<div class="abs btn" style="left:540px;top:847px;width:111px;height:36px;line-height:36px">Read More</div>

<!-- services -->
<section class="abs services"></section>
<h2 class="abs sec-title" style="top:958px">Our <span>Financial Services</span></h2>
<div class="abs divider" style="left:0;top:1008px;width:1200px">
  <div class="rule" style="left:433px;width:334px"></div>
  <div class="dot" style="left:578px"></div><div class="dot mid" style="left:596px"></div><div class="dot" style="left:614px"></div>
</div>
<svg class="abs" style="left:48px;top:1185px" width="22" height="38" viewBox="0 0 22 38"><path d="M20 2L3 19l17 17" stroke="#aaa" stroke-width="1.8" fill="none"/></svg>
<svg class="abs" style="left:1130px;top:1185px" width="22" height="38" viewBox="0 0 22 38"><path d="M2 2l17 17L2 36" stroke="#aaa" stroke-width="1.8" fill="none"/></svg>
<div class="abs svc-sep" style="left:341px"></div>
<div class="abs svc-sep" style="left:600px"></div>
<div class="abs svc-sep" style="left:866px"></div>

<div class="service" style="left:67px">
  <div class="ring"><svg width="44" height="44" viewBox="0 0 44 44"><rect x="8" y="6" width="26" height="32" rx="4" fill="var(--teal)"/><rect x="12" y="4" width="26" height="32" rx="4" fill="var(--teal)" stroke="#fff" stroke-width="1.5"/><text x="25" y="27" text-anchor="middle" font-family="Lato,sans-serif" font-weight="700" font-size="18" fill="#fff">$</text></svg></div>
  <h3>BOOKKEEPING</h3>
  <p>Lorem ipsum dolor sit amet,<br>consectetur adipiscing elit, sed do</p>
  <div class="btn">Read More</div>
</div>
<div class="service" style="left:330px">
  <div class="ring"><svg width="44" height="44" viewBox="0 0 44 44"><path d="M6 18l16-12 16 12v20H6z" fill="var(--teal)"/><rect x="13" y="12" width="18" height="16" fill="#fff"/><text x="22" y="25" text-anchor="middle" font-family="Lato,sans-serif" font-weight="700" font-size="13" fill="var(--teal)">$</text><path d="M6 20l16 11 16-11" stroke="#fff" stroke-width="1.5" fill="none"/></svg></div>
  <h3>ACCOUNTS PAYABLE</h3>
  <p>Lorem ipsum dolor sit amet,<br>consectetur adipiscing elit, sed do</p>
  <div class="btn">Read More</div>
</div>
<div class="service" style="left:594px">
  <div class="ring"><svg width="50" height="44" viewBox="0 0 50 44"><text x="29" y="17" text-anchor="middle" font-family="Lato,sans-serif" font-weight="700" font-size="17" fill="var(--teal)">$</text><path d="M3 28c6-2 11-4 17-1h10c2 0 2 3 0 3h-9c6 1 12 0 20-6 2-1 4 1 2 3-8 7-16 10-25 9l-15-2z" fill="var(--teal)"/></svg></div>
  <h3>ACCOUNTS RECEIVABLE</h3>
  <p>Lorem ipsum dolor sit amet,<br>consectetur adipiscing elit, sed do</p>
  <div class="btn">Read More</div>
</div>
<div class="service" style="left:862px">
  <div class="ring"><svg width="44" height="44" viewBox="0 0 44 44"><rect x="9" y="6" width="26" height="33" rx="3" fill="none" stroke="var(--teal)" stroke-width="2.5"/><rect x="13" y="11" width="18" height="7" fill="var(--teal)"/><g fill="var(--teal)"><rect x="13" y="22" width="4" height="4"/><rect x="20" y="22" width="4" height="4"/><rect x="27" y="22" width="4" height="4"/><rect x="13" y="29" width="4" height="4"/><rect x="20" y="29" width="4" height="4"/><rect x="27" y="29" width="4" height="4"/></g></svg></div>
  <h3>MANAGEMENT ACCOUNTING</h3>
  <p>Lorem ipsum dolor sit amet,<br>consectetur adipiscing elit, sed do</p>
  <div class="btn">Read More</div>
</div>

<!-- testimonials -->
<h2 class="abs col-title" style="left:101px;top:1416px">Client <span>Testimonials</span></h2>
<svg class="abs" style="left:545px;top:1448px" width="34" height="16" viewBox="0 0 34 16"><circle cx="8" cy="8" r="6" fill="none" stroke="var(--teal)" stroke-width="1.4"/><path d="M9.5 5l-3 3 3 3" stroke="var(--teal)" stroke-width="1.3" fill="none"/><circle cx="25" cy="8" r="6" fill="none" stroke="var(--teal)" stroke-width="1.4"/><path d="M23.5 5l3 3-3 3" stroke="var(--teal)" stroke-width="1.3" fill="none"/></svg>
<div class="abs divider" style="left:101px;top:1466px;width:476px">
  <div class="dot" style="left:0"></div><div class="dot mid" style="left:18px"></div><div class="dot" style="left:36px"></div>
  <div class="rule" style="left:52px;width:424px"></div>
</div>
<div class="abs quote-box"></div>
<svg class="abs" style="left:478px;top:1757px" width="60" height="34" viewBox="0 0 60 34"><path d="M0 1h60L8 32z" fill="#fafafa"/><path d="M0 1L8 32 60 1" stroke="#e0e0e0" stroke-width="1.2" fill="none"/></svg>
<p class="abs quote-text"><span class="quote-mark">“</span> Lorem ipsum dolor sit amet consetug e sed diay nibh euismodl tincidunt ut laoreet dolore magam er vol wisi enim ad minim veniam quis nostrud exerci tationorem ipsum dolor sit ametee sed diammmy nibh euismd tincidunt ut laoreet dolore magna aliqur volpatl tiidunt ut laoreet dolore magna aliqur volpatl Lorem ipsum dolor sit amet consetug e sed diay nibh euismodl tincidunt ut laoreet dolore magam er vol <span class="quote-mark">”</span></p>
<div class="abs avatar" role="img" aria-label="Portrait photo of the client"></div>
<div class="abs client-name">Mr. Owen Hartley</div>

<!-- quick contact -->
<h2 class="abs col-title" style="left:758px;top:1416px">Quick <span>Contact</span></h2>
<div class="abs divider" style="left:758px;top:1466px;width:343px">
  <div class="dot" style="left:0"></div><div class="dot mid" style="left:18px"></div><div class="dot" style="left:36px"></div>
  <div class="rule" style="left:52px;width:291px"></div>
</div>
<div class="abs field" style="top:1520px">Name</div>
<div class="abs field" style="top:1562px">Email</div>
<div class="abs field" style="top:1605px">Phone</div>
<div class="abs field" style="top:1647px">Contry</div>
<div class="abs field" style="top:1689px;height:88px">Comment</div>
<div class="abs btn submit">Submit</div>

<!-- partners -->
<section class="abs partners"></section>
<h2 class="abs sec-title" style="top:1901px">Our <span>Partners</span></h2>
<div class="abs divider" style="left:0;top:1950px;width:1200px">
  <div class="rule" style="left:500px;width:200px"></div>
  <div class="dot" style="left:578px"></div><div class="dot mid" style="left:596px"></div><div class="dot" style="left:614px"></div>
</div>
<svg class="abs" style="left:58px;top:2036px" width="20" height="34" viewBox="0 0 20 34"><path d="M17 2L3 17l14 15" stroke="#d5e4e8" stroke-width="3" fill="none"/></svg>
<svg class="abs" style="left:1120px;top:2036px" width="20" height="34" viewBox="0 0 20 34"><path d="M3 2l14 15L3 32" stroke="#d5e4e8" stroke-width="3" fill="none"/></svg>
<div class="abs badge" style="left:101px;width:177px"><i></i></div>
<div class="abs badge" style="left:304px;width:179px"><i></i></div>
<div class="abs badge" style="left:511px;width:178px"><i></i></div>
<div class="abs badge" style="left:715px;width:179px"><i></i></div>
<div class="abs badge" style="left:920px;width:179px"><i></i></div>

<!-- footer -->
<footer class="abs footer"></footer>
<div class="abs f-vsep" style="left:250px"></div>
<div class="abs f-vsep" style="left:550px"></div>
<div class="abs f-vsep" style="left:928px"></div>

<div class="abs" style="left:101px;top:2184px;width:112px">
  <div class="f-title">Quick Links</div>
  <ul class="f-list"><li>Home</li><li>About Us</li><li>Services</li><li>Experience</li><li>Resources</li><li>Contact Us</li></ul>
</div>

<div class="abs" style="left:293px;top:2184px;width:190px">
  <div class="f-title">Contact Detail</div>
  <p class="f-text" style="margin-top:10px"><b>401, Daltonby Bookkeeping</b><br>Lorem ipsum dolor sitak amet,<br>conse.</p>
  <p class="f-text" style="margin-top:11px;display:flex;align-items:center;gap:8px"><svg width="11" height="11" viewBox="0 0 20 20"><path d="M3 1l5 5-2 2.5c1.3 2.8 3 4.6 5.5 5.5L14 12l5 5-3 3C8 19 1 12 0 4z" fill="var(--sky)"/></svg>+123 456 7890</p>
  <p class="f-text" style="margin-top:4px;display:flex;align-items:center;gap:8px"><svg width="12" height="9" viewBox="0 0 12 9"><rect width="12" height="9" fill="var(--sky)"/><path d="M0 0l6 5 6-5" stroke="#2e2e2e" fill="none"/></svg>info@daltonbybookkeeping.com</p>
</div>

<div class="abs" style="left:613px;top:2184px;width:250px">
  <div class="f-title">Newsletter Signup</div>
  <p class="f-text" style="margin-top:10px;width:130px">Get the latest updates by entering your email address</p>
</div>
<div class="abs news-art" role="img" aria-label="Paper plane illustration"></div>
<div class="abs news-input"><svg class="abs" style="left:10px;top:12px" width="12" height="9" viewBox="0 0 12 9"><rect width="12" height="9" fill="#aaa"/><path d="M0 0l6 5 6-5" stroke="#fff" fill="none"/></svg>Enter your email</div>
<div class="abs news-btn">SUBSCRIBE</div>

<div class="abs" style="left:992px;top:2184px;width:105px">
  <div class="f-title">Follow Us</div>
  <div style="margin-top:2px">
    <div class="social"><i></i>SOCIALINE</div>
    <div class="social"><i></i>CHIRPWIRE</div>
    <div class="social"><i></i>CIRCLENET</div>
    <div class="social"><svg width="14" height="14" viewBox="0 0 14 14"><circle cx="2.5" cy="11.5" r="2" fill="#fff"/><path d="M1 6a7 7 0 0 1 7 7M1 1.5A11.5 11.5 0 0 1 12.5 13" stroke="#fff" stroke-width="2" fill="none"/></svg>RSS FEED</div>
  </div>
</div>

<div class="abs footer-base">
  <span class="abs" style="left:101px;top:14px">Copyright © 2016 Daltonby Bookkeeping. All Rights Reserved</span>
  <span class="abs" style="left:859px;top:14px">Terms &amp; Conditions &nbsp;&nbsp;&nbsp;|&nbsp;&nbsp;&nbsp; Privacy Policy</span>
</div>

</body>
</html>
```